(2) Trifold Brochures needed for automation industry

Need “Two” Trifold brochures. (files included) please see READ ME word doc attached.
1# will be for Pharmaceutical and Biotech companies. (stock photos and copy should be ALL pharma and biotech related.
#2 will be for food and beverage processing, Packaging & Distribution Center, Automotive, Chemical, Consumer Electronics, Government, Pulp & paper, Oil/Gas, Security & Detention, Water & Wastewater
Target Market(s)
automation industry - USA and Canada
Font styles to use
Serif
Requirements
Must have
- Target audience appeal. See attached Word file for ideas and details.
Nice to have
- Best looking Trifold Brochures in the industry
Should not have
- Cheap look

```html
<!DOCTYPE html>
<html lang="en">
<head>
<meta charset="utf-8">
<title>Corvane Automation – Trifold Inside Spread</title>
<link rel="stylesheet" href="https://fonts.googleapis.com/css2?family=Fira+Sans:wght@300;400;700&display=swap">
<style>
  :root {
    --backdrop: #4a4a4a;
    --navy-top: #0b1a55;
    --navy-mid: #0a1540;
    --navy-deep: #080d1f;
    --indigo: #2e2f98;
    --indigo-top: #0f2c70;
    --orange: #f47b20;
    --band-green: #b9d59a;
    --band-blue: #1a4a86;
    --text: #ffffff;
    --text-soft: #e4e8f4;
  }
  * { box-sizing: border-box; margin: 0; padding: 0; }
  html, body {
    width: 1200px; height: 1004px; overflow: hidden;
    background: var(--backdrop);
  }
  .brochure {
    position: absolute; left: 157px; top: 63px;
    width: 886px; height: 878px;
    font-family: "Fira Sans", sans-serif;
    color: var(--text);
    overflow: hidden;
  }
  .band {
    position: absolute; left: 0; width: 100%; height: 9px; display: flex;
  }
  .band--top { top: 0; }
  .band--bottom { bottom: 0; }
  .band span { flex: 1; }
  .band .band-left { background: linear-gradient(90deg, var(--band-green), var(--band-blue)); }
  .band .band-mid { background: var(--orange); }
  .band .band-right { background: linear-gradient(90deg, var(--band-blue), var(--band-green)); }

  .panel {
    position: absolute; left: 0; top: 9px; width: 886px; height: 494px;
    background: linear-gradient(180deg, var(--navy-top) 0%, var(--navy-mid) 45%, var(--navy-deep) 100%);
  }
  .panel svg { position: absolute; left: 0; top: 0; }
  .network-art {
    position: absolute; left: 0; top: 150px; width: 570px; height: 344px;
    background:
      radial-gradient(ellipse 55% 45% at 25% 65%, rgba(60,140,230,0.35), transparent 70%),
      radial-gradient(ellipse 50% 25% at 70% 25%, rgba(70,150,240,0.25), transparent 70%);
  }

  .col { position: absolute; top: 77px; }
  .col--serve { left: 27px; width: 250px; }
  .col--do { left: 314px; width: 240px; }
  .col--scada { left: 610px; width: 250px; }

  .heading {
    font-weight: 700; font-size: 34px; line-height: 1;
    letter-spacing: 0.01em; margin-bottom: 22px;
  }
  .col--do .heading, .col--scada .heading { margin-left: 0; }
  .body {
    font-weight: 300; font-size: 9px; line-height: 15.4px;
    color: var(--text-soft); margin-bottom: 15.4px;
  }
  .col--do .body { margin-left: 6px; text-align: justify; width: 231px; }
  .col--serve .body { text-align: justify; width: 246px; }
  .body:last-of-type { margin-bottom: 0; }

  .industries {
    list-style: none; margin: 12px 0 0 56px;
    font-weight: 300; font-size: 9px; line-height: 13.3px; letter-spacing: 0.05em;
  }
  .industries li::before, .features li::before {
    content: ""; display: inline-block; width: 3.5px; height: 3.5px;
    background: var(--text); margin-right: 5px; vertical-align: 1.5px;
  }

  .features {
    list-style: none; margin: 12px 0 0 30px; width: 215px;
    font-weight: 300; font-size: 8.8px; line-height: 12.8px; letter-spacing: 0.05em;
  }
  .features li { margin-bottom: 13px; }

  .photo-mosaic {
    position: absolute; left: 0; top: 503px; width: 886px; height: 366px;
  }
</style>
</head>
<body>
<main class="brochure">
  <div class="band band--top"><span class="band-left"></span><span class="band-mid"></span><span class="band-right"></span></div>

  <section class="panel">
    <svg width="886" height="494" viewBox="0 0 886 494" aria-hidden="true">
      <defs>
        <linearGradient id="scadaField" x1="0" y1="0" x2="0.3" y2="1">
          <stop offset="0" stop-color="#0f2c70"/>
          <stop offset="0.5" stop-color="#22318a"/>
          <stop offset="1" stop-color="#2e2f9a"/>
        </linearGradient>
      </defs>
      <polygon points="426,0 886,0 886,494 700,494" fill="url(#scadaField)"/>
    </svg>
    <div class="network-art" role="img" aria-label="Glowing blue hexagonal network illustration"></div>

    <div class="col col--serve">
      <h2 class="heading">WHO WE SERVE</h2>
      <p class="body">We provide both in-house and on-site service to a wide array of industries, specializing in but not limited to pharmaceutical.</p>
      <p class="body">Some of the industries we serve are:</p>
      <ul class="industries">
        <li>Pharmaceutical &amp; Biotech</li>
        <li>Food and beverage processing</li>
        <li>Packaging &amp; Distribution Center</li>
        <li>Automotive</li>
        <li>Chemical</li>
        <li>Consumer Electronics</li>
        <li>Government</li>
        <li>Pulp &amp; paper</li>
        <li>Oil/Gas</li>
        <li>Security &amp; Detention</li>
        <li>Water &amp; Wastewater</li>
      </ul>
    </div>

    <div class="col col--do">
      <h2 class="heading">WHAT WE DO</h2>
      <p class="body">We provide high-quality and cutting-edge solutions in automation. Whether it’s simple instruments or fully automated manufacturing lines, we have the solution for you. From conceptualization to implementation – We are here for you every step of the way.</p>
      <p class="body">We offer tailor-made automated solutions to consumers across the globe. From simple instruments to fully automated lines, from consumer goods to pharmaceutical manufacturing, we have everything that you have been looking for in automation.</p>
      <p class="body">Our team of first-class professionals is dedicated to designing industrial solutions that optimize processes consistently and accurately. We ensure that ongoing alterations and enhancements of approaches and procedures occur smoothly and seamlessly. We match your unique needs to unique, long-term solutions.</p>
    </div>

    <div class="col col--scada">
      <h2 class="heading">SCADA</h2>
      <p class="body">Corvane offers full turn key installations and integration for your existing SCADA equipment and software.</p>
      <ul class="features">
        <li>With server redundancy offering user administration and authentication.</li>
        <li>Our network encryption protect projects are clients from data loss and unauthorized access.</li>
        <li>Easy navigation, user friendly interface, spending less time navigating.</li>
        <li>Simpler workflow with decreased operator errors</li>
        <li>Third-party integration with a direct connection while reducing costs and waste.</li>
        <li>Realize efficiency gains across various systems.</li>
        <li>Increase availability and lengthen the lifecycle of assets.</li>
        <li>Improve equipment performance.</li>
        <li>Reduce maintenance costs.</li>
      </ul>
    </div>
  </section>

  <svg class="photo-mosaic" viewBox="0 0 886 366" role="img" aria-label="Mosaic of triangular photos showing engineers at control panels, automated process equipment and factory floors">
    <defs>
      <linearGradient id="mosaicFade" x1="0" y1="0" x2="0" y2="1">
        <stop offset="0.6" stop-color="#0b1450" stop-opacity="0"/>
        <stop offset="1" stop-color="#0b1450" stop-opacity="0.85"/>
      </linearGradient>
    </defs>
    <rect width="886" height="366" fill="#5d6b86"/>
    <polygon points="0,0 165,0 85,145 0,145" fill="#8a96a8"/>
    <polygon points="165,0 430,0 350,145 85,145" fill="#3b4a7a"/>
    <polygon points="430,0 596,0 596,145 350,145" fill="#8c8f96"/>
    <polygon points="596,0 700,0 620,145 596,145" fill="#7a7f88"/>
    <polygon points="700,0 886,0 886,145 620,145" fill="#56627a"/>
    <polygon points="0,145 85,145 0,300" fill="#6c7690"/>
    <polygon points="85,145 210,145 235,366 40,366 0,300" fill="#6a6c66"/>
    <polygon points="210,145 350,145 380,200 300,366 235,366" fill="#4d6a98"/>
    <polygon points="350,145 530,145 560,250 500,366 300,366 380,200" fill="#8a8783"/>
    <polygon points="530,145 620,145 700,145 650,260 560,250" fill="#4e5d92"/>
    <polygon points="560,250 650,260 600,366 500,366" fill="#3e4f88"/>
    <polygon points="700,145 886,145 886,366 600,366 650,260" fill="#7a7e84"/>
    <rect width="886" height="366" fill="url(#mosaicFade)"/>
  </svg>

  <div class="band band--bottom"><span class="band-left"></span><span class="band-mid"></span><span class="band-right"></span></div>
</main>
</body>
</html>
```